Book Cover Design for Humorous Dystopian Novel

RIDING MARLIN is an odd, humorous, sci-fi novel, blended with mystery, that doesn't necessarily fit into any genre, which is why it's been difficult to find a proper cover design over the past year.
It may be best to provide the book blurb to give you an idea for a concept:
On the run. Out of time. A brownie recipe worth millions.
Lovable loser Derek waits tables by day and dreams of making something better of himself by night. But, under the almighty, oppressive rule of The Quorum and their divisive caste system, it's nearly impossible. That is until his super-geek pal and fellow waiter, Sprocket, hits upon a foolproof scheme: steal their employer's ultra-popular, top secret recipes and sell them on a black market internet site.
It's all fun and games until the mysterious death of a local hacker shatters their surefire plan, sending them on a fast-paced adventure through the city's seedy underground, where they hope to salvage what's left and avoid capture by The Quorum Agents at all costs. Nobody comes back from that. Nobody.
-
I would like to see designs that are light, fun, and have a sci-fi feel, but also capture the idea that this is really just a book about two desperate waiters trying to steal some top-secret recipes and sell them on the internet.
The book is available on Pellorix if you would like to read a sample to get a better feel for the story.
Cover sizing/quality requirements for the ebook:
jpg format
1.6 ratio, or for best quality, a size of 1563x2500
300 dpi
Target Market(s)
Younger adults, primarily ages 20-40. Hip and interested in fun reads.
Industry/Entity Type
Internet
Look and feel

```html
<!DOCTYPE html>
<html lang="en">
<head>
<meta charset="utf-8">
<title>Riding Marlin – Book Cover</title>
<link rel="stylesheet" href="https://fonts.googleapis.com/css2?family=Righteous&family=Open+Sans:wght@400;700&display=swap">
<style>
  :root {
    --page: #efefef;
    --cover-orange: #e05f1e;
    --cover-orange-deep: #d2561a;
    --title-white: #fbf6ef;
    --title-glow: #f49a4e;
    --title-edge: #b84510;
    --body-text: #f7d9c2;
    --box-dark: #6e2409;
    --box-text: #f3c9a8;
    --art-light: #d9a37a;
    --art-mid: #b8683a;
    --art-dark: #7a3512;
    --figure-shadow: #9c3b0e;
  }
  * { margin: 0; padding: 0; box-sizing: border-box; }
  html, body { width: 1200px; height: 800px; overflow: hidden; background: var(--page); }
  body { position: relative; font-family: "Open Sans", Arial, sans-serif; }

  .book-wrap {
    position: absolute; left: 170px; top: 90px;
    display: flex; height: 620px;
    box-shadow: 0 10px 30px rgba(0,0,0,0.18);
  }
  .back-cover, .front-cover, .spine {
    position: relative; height: 100%;
    background: var(--cover-orange);
  }
  .back-cover { width: 400px; }
  .spine { width: 60px; background: var(--cover-orange-deep); border-left: 1px solid rgba(0,0,0,0.12); border-right: 1px solid rgba(0,0,0,0.12); }
  .front-cover { width: 400px; overflow: hidden; }

  .book-title {
    font-family: "Righteous", "Arial Black", sans-serif;
    color: var(--title-white);
    text-align: center;
    line-height: 0.95;
    letter-spacing: 1px;
    text-shadow:
      0 0 2px var(--title-edge),
      0 0 6px var(--title-glow),
      0 0 10px var(--title-glow);
  }

  /* back cover */
  .back-author {
    position: absolute; top: 18px; left: 0; right: 0;
    text-align: center; font-weight: 700; font-size: 15px; color: var(--title-white);
  }
  .back-cover .book-title { position: absolute; top: 42px; left: 0; right: 0; font-size: 60px; }
  .blurb {
    position: absolute; top: 200px; left: 26px; right: 26px;
    font-size: 10.5px; line-height: 15px; color: var(--body-text);
    text-align: justify; text-align-last: center;
  }
  .back-box {
    position: absolute; bottom: 22px; width: 110px; height: 56px;
    background: var(--box-dark); color: var(--box-text);
    display: flex; align-items: center; justify-content: center;
    font-size: 11px;
  }
  .logo-box { left: 30px; }
  .isbn-box { right: 30px; }

  /* spine */
  .spine-text {
    position: absolute; left: 50%; top: 0;
    writing-mode: vertical-rl;
    transform: translateX(-50%);
    white-space: nowrap;
  }
  .spine-title { top: 40px; font-size: 34px; }
  .spine-author {
    top: 440px; font-weight: 700; font-size: 15px; color: var(--title-white);
    text-shadow: 0 0 4px var(--title-edge);
  }

  /* front cover */
  .front-cover .book-title { position: absolute; top: 28px; left: 0; right: 0; font-size: 76px; }
  .front-author {
    position: absolute; right: 20px; bottom: 42px;
    font-weight: 700; font-size: 18px; color: var(--title-white);
    text-shadow: 0 0 4px var(--title-edge);
    z-index: 2;
  }
  .lead-waiter-art {
    position: absolute; left: 22px; top: 240px; width: 218px; height: 380px;
    border-radius: 100px 100px 0 0;
    background: linear-gradient(180deg, var(--art-light) 0%, var(--art-mid) 55%, var(--art-dark) 100%);
  }
  .host-shadow {
    position: absolute; left: 278px; top: 452px; width: 112px; height: 34px;
    border-radius: 50%; background: var(--figure-shadow);
  }
  .host-waiter-art {
    position: absolute; left: 290px; top: 225px; width: 96px; height: 245px;
    border-radius: 40px 40px 6px 6px;
    background: linear-gradient(180deg, var(--art-light) 0%, var(--art-mid) 60%, var(--art-dark) 100%);
  }
</style>
</head>
<body>
  <div class="book-wrap">
    <section class="back-cover">
      <div class="back-author">Author Name</div>
      <h2 class="book-title">RIDING<br>MARLIN</h2>
      <p class="blurb">Lorem ipsum dolor sit amet, consectetur adipisicing elit, sed do eiusmod tempor incididunt ut labore et dolore magna aliqua. Ut enim ad minim veniam, quis nostrud exercitation. Lorem ipsum dolor sit amet, consectetur adipisicing elit, sed do eiusmod tempor incididunt ut labore et dolore magna aliqua. Ut enim ad minim veniam, quis nostrud exercitation. Lorem ipsum dolor sit amet, consectetur adipisicing elit, sed do eiusmod tempor incididunt ut labore et dolore magna aliqua. Ut enim ad minim veniam, quis nostrud exercitation. Lorem ipsum dolor sit amet, consectetur adipisicing elit, sed do eiusmod tempor incididunt ut labore et dolore magna aliqua. Ut enim ad minim veniam, quis nostrud exercitation. Lorem ipsum dolor sit amet, consectetur adipisicing elit, sed do eiusmod tempor incididunt ut labore et dolore magna aliqua. Ut enim ad minim veniam, quis nostrud exercitation. Lorem ipsum dolor sit amet, consectetur adipisicing elit, sed do eiusmod tempor incididunt ut labore et dolore magna aliqua. Ut enim ad minim veniam, quis nostrud exercitation.</p>
      <div class="back-box logo-box">LOGO</div>
      <div class="back-box isbn-box">ISBN</div>
    </section>

    <section class="spine">
      <div class="spine-text book-title spine-title">RIDING MARLIN</div>
      <div class="spine-text spine-author">Author Name</div>
    </section>

    <section class="front-cover">
      <h1 class="book-title">RIDING<br>MARLIN</h1>
      <div class="host-shadow"></div>
      <div class="host-waiter-art" role="img" aria-label="Illustration of a moustached head waiter in a white jacket carrying a tray"></div>
      <div class="lead-waiter-art" role="img" aria-label="Illustration of a winking waiter in a black vest and apron writing on an order pad"></div>
      <div class="front-author">Author Name</div>
    </section>
  </div>
</body>
</html>
```